Hello,
Is it possible for your graphic designer to prepare two exhibition walls for us according to the attachment? Graphics for panels - fig. B1-B2 (panel dimensions and stand visualization attached "PAVILLION POLOGNE (TRELDAX)-V02.pdf").
and the logo according to the guidelines in the drawing, marking A1. Graphics according to the last roll-ups that were prepared by you (template in the attachment) with one change.

Industry/Entity Type

aviation industry

Colors
0054AA
0677BA
7BADD7
CADEEF
E8F1F8
EE7325
F08F49
F5BC92
FAE3D3
FDF4ED

Requirements
Must have
• logo, www

```html
<!DOCTYPE html>
<html lang="en">
<head>
<meta charset="UTF-8">
<title>Vorantek Roll-up Banners</title>
<link rel="stylesheet" href="https://fonts.googleapis.com/css2?family=Montserrat:wght@600;700;800&family=Open+Sans:wght@400;600&display=swap">
<style>
:root{
  --blue-deep:#0054AA;
  --blue:#0677BA;
  --blue-mid:#7BADD7;
  --blue-light:#CADEEF;
  --blue-pale:#E8F1F8;
  --orange:#EE7325;
  --orange-mid:#F08F49;
  --orange-light:#F5BC92;
  --orange-pale:#FAE3D3;
  --cream:#FDF4ED;
  --ink:#1f2a3a;
  --stage:#eceef1;
}
*{box-sizing:border-box;margin:0;padding:0}
html,body{width:1200px;height:2732px;overflow:hidden}
body{background:var(--stage);font-family:"Open Sans",Arial,sans-serif;color:var(--ink);position:relative}
.banner{position:absolute;top:700px;width:560px;height:1332px;background:#fff;overflow:hidden;box-shadow:0 6px 24px rgba(0,40,90,.15)}
.banner--left{left:27px}
.banner--right{left:613px}
.banner__header{position:absolute;left:0;top:0;width:100%;height:150px}
.banner__header-shape{position:absolute;inset:0}
.brand{position:absolute;left:34px;top:52px;display:flex;align-items:center;gap:12px}
.brand__square{width:34px;height:34px;background:var(--blue-deep)}
.brand__name{font-family:"Montserrat",Arial,sans-serif;font-weight:800;font-size:38px;letter-spacing:1px;color:var(--blue-deep)}
.banner--right .brand{left:auto;right:40px}
.banner--right .brand__square{background:#fff}
.banner--right .brand__name{color:#fff}
.banner__body{position:absolute;left:0;top:150px;width:100%;height:560px;background:linear-gradient(180deg,#fff 0%,var(--blue-pale) 100%)}
.feature{position:absolute;left:30px;right:30px}
.feature__thumb{position:absolute;left:0;top:0;width:86px;height:86px;border-radius:50%;border:4px solid var(--blue-light);background:radial-gradient(circle at 40% 40%,#f3f4f6,#9aa3ad)}
.feature__thumb--mask{background:radial-gradient(circle,#fff 0 30%,#7da63a 31% 70%,#e8ecef 71%)}
.feature__thumb--metal{background:radial-gradient(circle at 45% 45%,#e9ecef,#6f7781)}
.feature__thumb--regen{background:radial-gradient(circle at 50% 50%,#555 0 35%,#bfc5cc 36%)}
.feature__title{margin-left:104px;padding-top:14px;font-family:"Montserrat",Arial,sans-serif;font-weight:800;font-size:22px;line-height:1.15;color:var(--blue-deep);text-transform:uppercase}
.feature__title--mixed{text-transform:none}
.feature__text{margin:14px 0 0 104px;font-size:13px;line-height:1.55;color:#2f3b4c}
.badge{position:absolute;width:120px;height:40px;border:2px solid var(--blue-deep);border-radius:4px;background:#fff}
.badge::before{content:"";position:absolute;left:8px;top:8px;width:20px;height:20px;background:var(--orange)}
.stripes{position:absolute;left:0;width:100%;height:90px}
.photo{position:absolute;left:0;width:100%}
.photo--plane{top:770px;height:470px;background:linear-gradient(180deg,#9cc4e6 0%,#cfe1f0 45%,#d8dde2 62%,#8d949c 100%)}
.photo--engine{top:770px;height:470px;background:linear-gradient(160deg,#d9a86a 0%,#e9c891 30%,#8fa4b8 65%,#4b5a6c 100%)}
.footer{position:absolute;left:0;bottom:0;width:100%;height:92px;background:linear-gradient(90deg,var(--blue-deep),var(--blue));border-top:6px solid var(--orange);display:flex;align-items:center;justify-content:center}
.footer__www{font-family:"Montserrat",Arial,sans-serif;font-weight:700;font-size:26px;letter-spacing:1px;color:#fff;text-transform:uppercase}
</style>
</head>
<body>

<section class="banner banner--left">
  <header class="banner__header">
    <svg class="banner__header-shape" width="560" height="150" viewBox="0 0 560 150">
      <polygon points="400,0 560,0 560,150 470,150" fill="var(--blue-deep)"/>
      <polygon points="380,0 400,0 470,150 450,150" fill="var(--orange)"/>
    </svg>
    <div class="brand"><span class="brand__square"></span><span class="brand__name">VORANTEK</span></div>
  </header>
  <div class="banner__body">
    <article class="feature" style="top:30px">
      <div class="feature__thumb" role="img" aria-label="Machined metal test coupons"></div>
      <h2 class="feature__title">Coupons &amp; Substrates Machining</h2>
      <p class="feature__text">We specialise in manufacturing high-quality test coupons, substrates and samples for coating, thermal spray and plasma processes. Parts are machined to drawings from certified alloys, with full traceability and fast lead times for aerospace laboratories.</p>
    </article>
    <article class="feature" style="top:275px">
      <div class="feature__thumb feature__thumb--regen" role="img" aria-label="Regenerated coupon parts"></div>
      <h2 class="feature__title">Coupons Regeneration</h2>
      <p class="feature__text">Our regeneration service restores used coupons to their original specification. By removing the coating and regrinding the surface, we extend the life of each part and cut costs, with results that meet the same strict tolerances.</p>
    </article>
    <div class="badge" style="left:30px;top:505px"></div>
  </div>
  <svg class="stripes" style="top:700px" width="560" height="90" viewBox="0 0 560 90">
    <polygon points="0,40 560,0 560,14 0,54" fill="var(--orange)"/>
    <polygon points="0,62 560,22 560,30 0,70" fill="var(--blue-mid)"/>
  </svg>
  <div class="photo photo--plane" role="img" aria-label="Passenger jet on a runway under a blue sky"></div>
  <footer class="footer"><span class="footer__www">www.vorantek.com</span></footer>
</section>

<section class="banner banner--right">
  <header class="banner__header">
    <svg class="banner__header-shape" width="560" height="150" viewBox="0 0 560 150">
      <defs><linearGradient id="hdr" x1="0" y1="0" x2="1" y2="0"><stop offset="0" stop-color="#0054AA"/><stop offset="1" stop-color="#0677BA"/></linearGradient></defs>
      <polygon points="0,0 560,0 560,150 0,110" fill="url(#hdr)"/>
      <polygon points="0,110 560,150 560,156 0,118" fill="var(--orange)"/>
    </svg>
    <div class="brand"><span class="brand__square"></span><span class="brand__name">VORANTEK</span></div>
  </header>
  <div class="banner__body">
    <article class="feature" style="top:30px">
      <div class="feature__thumb feature__thumb--mask" role="img" aria-label="Reusable silicone masking ring"></div>
      <h2 class="feature__title">Reusable Silicone Masking Hard Masking</h2>
      <p class="feature__text">Designed for repeatable masking in thermal spray and plasma coating lines, our silicone masks protect critical surfaces, fit precisely and can be reused for many cycles, saving time and material.</p>
    </article>
    <article class="feature" style="top:275px">
      <div class="feature__thumb feature__thumb--metal" role="img" aria-label="High-temperature metal fixtures"></div>
      <h2 class="feature__title feature__title--mixed">High-temperature Custom Metal Accessories</h2>
      <p class="feature__text">Custom accessories for high-temperature equipment, such as hooks, couplings, fixtures and holders, made of heat-resistant alloys that keep their shape and strength at temperatures up to 1100°C.</p>
    </article>
    <div class="badge" style="left:30px;top:505px"></div>
  </div>
  <svg class="stripes" style="top:700px" width="560" height="90" viewBox="0 0 560 90">
    <polygon points="0,0 560,40 560,54 0,14" fill="var(--orange)"/>
    <polygon points="0,22 560,62 560,70 0,30" fill="var(--blue-mid)"/>
  </svg>
  <div class="photo photo--engine" role="img" aria-label="Aircraft jet engine in a maintenance hangar"></div>
  <footer class="footer"><span class="footer__www">www.vorantek.com</span></footer>
</section>

</body>
</html>
```